依頼詳細
駅前で配布するフライヤーの作成をお願いいたします。
韓流をイメージさせるようなポップなデザインを期待しております。
表面は店名のロゴメインでごちゃごちゃさせずに、裏面はリゾート感を押し出していただけたらと思っております。

記載項目
表面は店名のロゴのみ。
裏面は、以下の内容を記載してください。

Free drink ¥3,500 (Tax in ¥3,850円) / 1h

Cast drink ¥1,000 (Tax in ¥1,100) ~

Foods ¥700 (Tax in ¥770) ~

Address 兵庫県神戸市中央区若葉坂3丁目7-25 白樺テラスビル 4階
Phone 090-7264-3951

※上記金額にサービス料1名様10%、2名様以上5%を頂戴いたします。

上記住所より地図も作成してください。
サイズ
A6
ページ数
両面
希望イメージ
シンプル 複雑
単色 カラフル
暗い 明るい
日常 高級
遊び心 厳粛
未来的 伝統的
女性的 男性的
希望する色
赤系、黄・オレンジ系、韓国にあるような、蛍光管のポップな原色系
納品ファイル
• 高解像度JPG (.jpg)
• イラストレーター形式 (.ai)
補足説明
ネオンサイン例です。
ネオンサイン例です。
リアルな蛍光管のようなデザインが希望です。
Café&Barは業態の表示ですので、そこまで大きくせず、店名である『87』をもっと全面に押し出していただければ。

あと、裏面も表面と同じようなデザインでお願いします。
■ 選んだ理由

イメージとぴったりでした。

■ 提案者全員のお礼・コメント

今回は弊社コンペにご参加いただきありがとうございます。

魅力的な提案ばかりで選定に苦労いたしましたが、表面、裏面のイメージがピッタリな提案者の方にきめさせていただきました。

ありがとうございました。

```html
<!DOCTYPE html>
<html lang="ja">
<head>
<meta charset="UTF-8">
<title>Cafe &amp; Bar 87</title>
<link rel="stylesheet" href="https://fonts.googleapis.com/css2?family=Nunito:wght@700;800&display=swap">
<style>
  :root {
    --wall-light: #3b3b3b;
    --wall-dark: #121212;
    --neon-yellow: #ffe27a;
    --neon-yellow-glow: #ffb400;
    --neon-orange: #ffb27f;
    --neon-orange-glow: #ff6a1f;
    --glass-pink: #d94bd0;
    --glass-gold: #f4b03a;
  }
  html, body {
    margin: 0;
    padding: 0;
    overflow: hidden;
    background: var(--wall-dark);
  }
  .flyer {
    position: relative;
    width: 849px;
    height: 1200px;
    overflow: hidden;
    background:
      radial-gradient(ellipse at 50% 40%, var(--wall-light) 0%, #262626 55%, var(--wall-dark) 100%);
    font-family: "Nunito", sans-serif;
  }
  .business-type {
    position: absolute;
    top: 180px;
    left: 0;
    width: 100%;
    margin: 0;
    text-align: center;
    font-size: 112px;
    font-weight: 700;
    letter-spacing: 2px;
    color: var(--neon-yellow);
    text-shadow:
      0 0 6px var(--neon-yellow),
      0 0 18px var(--neon-yellow-glow),
      0 0 40px var(--neon-yellow-glow);
  }
  .cocktail-art {
    position: absolute;
    top: 396px;
    left: 272px;
    width: 410px;
    height: 346px;
    border-radius: 40px;
    background:
      radial-gradient(ellipse at 35% 55%, rgba(217, 75, 208, 0.35) 0%, rgba(217, 75, 208, 0) 60%),
      radial-gradient(ellipse at 70% 35%, rgba(244, 176, 58, 0.35) 0%, rgba(244, 176, 58, 0) 60%);
  }
  .shop-number {
    position: absolute;
    top: 780px;
    left: 0;
    width: 100%;
    margin: 0;
    text-align: center;
    font-size: 310px;
    line-height: 1;
    font-weight: 800;
    color: var(--neon-orange);
    text-shadow:
      0 0 8px var(--neon-orange),
      0 0 24px var(--neon-orange-glow),
      0 0 56px var(--neon-orange-glow);
  }
</style>
</head>
<body>
  <main class="flyer">
    <h2 class="business-type">Cafe &amp; Bar</h2>
    <div class="cocktail-art" role="img" aria-label="Neon-tube illustration of two cocktail glasses, a pink martini glass with a cherry and a gold glass with a lemon slice"></div>
    <h1 class="shop-number">87</h1>
  </main>
</body>
</html>
```